Business Image

I have recently had a new company logo made up and require some new business cards to go with it.

Target Market(s)

Developers & high worth clients.

Industry/Entity Type

Business

Contact Information for Business Card

The business is in the construction/management industry. It needs to be classy but have a industrial feel. I would like the business card to be a elegant presentation in itself.

Requirements
Must have
• Current logo & company name. Colouring needs to be the same as the current design also.
Nice to have
• A few different designs & presentations of single and double sided business cards.

```html
<!DOCTYPE html>
<html lang="en">
<head>
<meta charset="utf-8">
<title>Ironvale Build Group – Business Cards</title>
<link rel="stylesheet" href="https://fonts.googleapis.com/css2?family=Noto+Serif:wght@400;700&family=Roboto:wght@400;500&display=swap">
<style>
  :root {
    --backdrop: #e4e4e4;
    --card: #2b2b29;
    --brand-blue: #62b3e2;
    --text-light: #f1f1f1;
    --text-muted: #d6d6d6;
  }
  * { margin: 0; padding: 0; box-sizing: border-box; }
  html, body {
    width: 1200px; height: 576px; overflow: hidden;
    background: var(--backdrop);
  }
  .stage { position: relative; width: 1200px; height: 576px; }
  .card {
    position: absolute;
    width: 484px; height: 292px;
    background: var(--card);
    border-radius: 12px;
    overflow: hidden;
    box-shadow: 0 3px 6px rgba(0,0,0,.25);
  }
  .card--front { left: 82px; top: 139px; }
  .card--back { left: 602px; top: 138px; }

  .brand-mark { display: block; background: var(--brand-blue); }
  .brand-name {
    font-family: "Noto Serif", serif;
    font-weight: 700;
    color: var(--brand-blue);
    text-transform: uppercase;
    letter-spacing: 1px;
    line-height: 1.1;
    white-space: nowrap;
  }

  .card--front .brand-mark {
    position: absolute; left: 214px; top: 72px; width: 56px; height: 56px;
  }
  .card--front .brand-name {
    position: absolute; left: 0; right: 0; top: 146px;
    text-align: center; font-size: 28px;
  }

  .card--back .brand-mark {
    position: absolute; left: 36px; top: 44px; width: 64px; height: 64px;
  }
  .card--back .brand-name {
    position: absolute; left: 128px; top: 62px;
    font-size: 21px;
  }

  .holder { position: absolute; left: 32px; top: 206px; }
  .holder-name {
    font-family: "Noto Serif", serif; font-weight: 400;
    font-size: 19px; color: var(--brand-blue); line-height: 1.1;
  }
  .holder-role {
    font-family: "Roboto", sans-serif; font-size: 12px;
    color: var(--text-light); margin-top: 3px;
  }

  .contact {
    position: absolute; left: 258px; top: 170px;
    font-family: "Roboto", sans-serif; font-size: 13px;
    color: var(--text-light); line-height: 16px;
  }
  .contact-address { margin-bottom: 7px; }
  .contact-line { display: flex; align-items: center; gap: 12px; }
  .contact-line svg { width: 12px; height: 12px; fill: var(--text-muted); }

  .accent-band { position: absolute; left: 0; bottom: 0; width: 484px; height: 30px; }
  .website {
    position: absolute; left: 258px; bottom: 7px;
    font-family: "Roboto", sans-serif; font-size: 13px;
    color: #eaf5fb;
  }
</style>
</head>
<body>
<main class="stage">
  <section class="card card--front" aria-label="Card front">
    <span class="brand-mark"></span>
    <p class="brand-name">Ironvale<br>Build Group</p>
  </section>

  <section class="card card--back" aria-label="Card back">
    <span class="brand-mark"></span>
    <p class="brand-name">Ironvale Build Group</p>

    <div class="holder">
      <p class="holder-name">Mark Ellison</p>
      <p class="holder-role">Director</p>
    </div>

    <div class="contact">
      <p class="contact-address">48 Foundry Lane, Suite 2,<br>Harwick Bay, Northvale 204715</p>
      <p class="contact-line">
        <svg viewBox="0 0 24 24" aria-hidden="true"><path d="M2 9c0-4 4-6 10-6s10 2 10 6v2h-5V8H7v3H2zM5 13h14l2 8H3z"/></svg>
        555-0142-7788
      </p>
      <p class="contact-line">
        <svg viewBox="0 0 24 24" aria-hidden="true"><path d="M2 5h20v14H2zm2 2v1l8 5 8-5V7l-8 5z"/></svg>
        mark@ironvalebuild.com
      </p>
    </div>

    <svg class="accent-band" viewBox="0 0 484 30" preserveAspectRatio="none" aria-hidden="true">
      <path d="M0 16 H270 L288 0 H484 V30 H0 Z" fill="var(--brand-blue)"/>
    </svg>
    <p class="website">www.ironvalebuild.com</p>
  </section>
</main>
</body>
</html>
```